tarang dine in

we are thai, malaysian, vietnamese restaurant. Southeast Asia, we love antique, classic, cozy ambiance, and illustrate arts form.
I would like to design lunch,dinner and limited take out menu a classic, elegant, and fun menu, healthy earthy, feels like in southeast asia

attachment are some example files that you can review it
this is us www.lovetarang-example.com
would like to follow http://www.goldenlotusrowhome-example.com 's style

restaurants that around the coner,
www.zelbaroni-example.com
http://www.frondavel-example.com
http://www.lolahartleys-example.com
http://www.harborgrillkeystone-example.com

Target Market(s)

neighbourhood, BWC students, modern and hip

Other font styles liked:
• fonts that match my old menu

Colors
faa54b
fece3e
ebf1f7
acd037
ec2027
000000

Requirements
Nice to have
• insider tips: Don't waste money on lousy food = instant regret
• Keep Calm Curry On

```html
<!DOCTYPE html>
<html lang="en">
<head>
<meta charset="utf-8">
<title>tarang – Menu</title>
<link href="https://fonts.googleapis.com/css2?family=Arimo:wght@400;700&family=Josefin+Sans:wght@600;700&family=PT+Serif&display=swap" rel="stylesheet">
<style>
  :root {
    --page: #e3e7eb;
    --panel: #f0f2f4;
    --band: #dca35d;
    --orange: #e99b45;
    --yellow: #f2c443;
    --green: #acd037;
    --ink: #111111;
    --body: #2a2a2a;
  }
  html, body { margin: 0; padding: 0; overflow: hidden; }
  body { width: 849px; height: 1200px; background: var(--page); }
  .menu { position: relative; width: 849px; height: 1200px; overflow: hidden; background: var(--page); }

  .header-band { position: absolute; left: 0; top: 0; width: 849px; height: 102px; background: var(--band); }
  .ornament { position: absolute; top: 47px; width: 24px; height: 24px; }
  .ornament--left { left: 188px; }
  .ornament--right { left: 640px; }
  .brand { position: absolute; left: 0; top: 36px; width: 849px; text-align: center; }
  .brand-name { font-family: "Josefin Sans", sans-serif; font-weight: 700; font-size: 62px; line-height: 1; color: var(--ink); letter-spacing: 1px; }
  .brand-tagline { margin-top: 10px; font-family: "PT Serif", serif; font-size: 12px; letter-spacing: 1.5px; color: var(--ink); font-weight: 700; }

  .section { position: absolute; left: 41px; width: 785px; background: var(--panel); }
  .section--appetizers { top: 127px; height: 374px; }
  .section--noodles { top: 520px; height: 344px; }
  .section--soups { top: 879px; height: 293px; }
  .corner { position: absolute; width: 58px; height: 50px; }
  .corner--top { left: 0; top: 0; }
  .corner--bottom { right: 0; bottom: 0; }

  .section-heading { position: absolute; left: 0; top: 31px; width: 785px; height: 26px; }
  .section-heading::before { content: ""; position: absolute; left: 50px; right: 42px; top: 11px; height: 4px; background: var(--green); }
  .section-heading h2 { position: absolute; top: 0; margin: 0; padding: 0 16px; background: var(--panel);
    font-family: "Josefin Sans", sans-serif; font-weight: 600; font-size: 19px; line-height: 26px; color: var(--orange); text-transform: uppercase; letter-spacing: -0.6px; }
  .section--appetizers h2 { left: 206px; }
  .section--noodles h2 { left: 205px; }
  .section--soups h2 { left: 195px; }

  .column { position: absolute; top: 72px; }
  .column--left { left: 51px; width: 291px; }
  .column--right { left: 430px; width: 307px; }
  .section--noodles .column--left { width: 285px; }
  .section--soups .column--left { left: 52px; width: 284px; }
  .section--soups .column--right { left: 432px; width: 300px; }

  .item { position: relative; margin-bottom: 14px; }
  .item-name { margin: 0; width: 240px; font-family: "Arimo", sans-serif; font-weight: 400; font-size: 15.5px; line-height: 17px; color: var(--ink); }
  .column--right .item-name { width: 222px; }
  .section--soups .column--right .item-name { width: 250px; }
  .item-price { position: absolute; right: 0; top: 0; font-family: "Arimo", sans-serif; font-size: 15px; line-height: 17px; color: var(--orange); }
  .item-price--raised { top: -17px; }
  .item-desc { margin: 3px 0 0; width: 240px; font-family: "PT Serif", serif; font-size: 11px; line-height: 17px; color: var(--body); }
  .item-desc--wide { width: 258px; }
</style>
</head>
<body>
<div class="menu">
  <div class="header-band"></div>
  <svg class="ornament ornament--left" viewBox="0 0 24 24" role="img" aria-label="small flower ornament"><circle cx="12" cy="12" r="11" fill="#1a1a1a"/></svg>
  <svg class="ornament ornament--right" viewBox="0 0 24 24" role="img" aria-label="small flower ornament"><circle cx="12" cy="12" r="11" fill="#1a1a1a"/></svg>
  <div class="brand">
    <div class="brand-name">tarang</div>
    <div class="brand-tagline">SOUTHEAST ASIAN STREET FOOD</div>
  </div>

  <section class="section section--appetizers">
    <svg class="corner corner--top" viewBox="0 0 58 50"><polygon points="0,0 58,0 0,50" fill="var(--yellow)"/></svg>
    <svg class="corner corner--bottom" viewBox="0 0 58 50"><polygon points="58,0 58,50 0,50" fill="var(--yellow)"/></svg>
    <div class="section-heading"><h2>Appetizers</h2></div>
    <div class="column column--left">
      <div class="item"><h3 class="item-name">Roti Canai Velora</h3><span class="item-price">€5</span>
        <p class="item-desc">Handmade Malaysian crispy and fluffy roti dough, vegeterian dal dip</p></div>
      <div class="item"><h3 class="item-name">Classic Curry Potato Puff</h3><span class="item-price item-price--raised">€3</span>
        <p class="item-desc">Variety of spices, herbs, Meadowrun Hill potatoes or chicken (Togo whole piece 2.75)</p></div>
      <div class="item"><h3 class="item-name">Plump’s Dumplings</h3><span class="item-price">€6</span>
        <p class="item-desc">Pork, chive, smoked chilli oil, peanut sauce</p></div>
      <div class="item"><h3 class="item-name">BBQ Char Siu Bun</h3><span class="item-price">€7</span>
        <p class="item-desc">Roasted pork, Thai dark soy sauce, citrus-honey glazed, cucumber pickles, tomatoes, toasted sesame seeds</p></div>
    </div>
    <div class="column column--right">
      <div class="item"><h3 class="item-name">Malay Spring Rolls</h3><span class="item-price">€5</span>
        <p class="item-desc item-desc--wide">Jicama, carrot, cilantro, sweet chili dipping sauce</p></div>
      <div class="item"><h3 class="item-name">Thai Boneless Fried Chicken<br>Wings</h3><span class="item-price">€7</span>
        <p class="item-desc">Coconut milk, pandan leaves, Tumeric, Shaox-ing cooking wine hot &amp; spicy glazed</p></div>
      <div class="item"><h3 class="item-name">kaffil-lime lemongrass tumeric<br>mussles</h3><span class="item-price">€8</span>
        <p class="item-desc">Basil Lemongrass wok saute Mussles hand pounded chilli lemongrass paste</p></div>
      <div class="item"><h3 class="item-name">Malaysian Chicken<br>Satay Shis Kebab</h3><span class="item-price">€4</span>
        <p class="item-desc">Marinaded lemongrass seasonings, chacoaled chicken skewers, peanut sauce</p></div>
    </div>
  </section>

  <section class="section section--noodles">
    <svg class="corner corner--top" viewBox="0 0 58 50"><polygon points="0,0 58,0 0,50" fill="var(--yellow)"/></svg>
    <svg class="corner corner--bottom" viewBox="0 0 58 50"><polygon points="58,0 58,50 0,50" fill="var(--yellow)"/></svg>
    <div class="section-heading"><h2>Stir Fried &amp; Soup Noodles</h2></div>
    <div class="column column--left">
      <div class="item"><h3 class="item-name">Classic Pho Bò Hue</h3><span class="item-price">€11</span>
        <p class="item-desc">Beef meat ball, Vietnamese spices, cardamom pods, black peppercorn, chopped coriander leaf</p></div>
      <div class="item"><h3 class="item-name">Curry Laksa</h3><span class="item-price">€13</span>
        <p class="item-desc">Variety of spices, herbs, Meadowrun Hill potatoes or chicken (Togo whole piece 2.75)</p></div>
      <div class="item"><h3 class="item-name">Pho Ga</h3><span class="item-price">€10</span>
        <p class="item-desc">Shredded chicken noodle soup, crispy fried shal-lots, cilantro, scallion, green chili, white pepper</p></div>
      <div class="item"><h3 class="item-name">Pad Thai</h3><span class="item-price">€10</span>
        <p class="item-desc">Sweet radish, egg, chives, beansprout, roasted peanut, fresh lime, paprika</p></div>
    </div>
    <div class="column column--right">
      <div class="item"><h3 class="item-name">Pad Kee Mao</h3><span class="item-price">€10</span>
        <p class="item-desc">Fresh flat Chow Fun, tomatoes, Birdseye chilli, onion, bell pepper, basil leaves</p></div>
      <div class="item"><h3 class="item-name">Coconut Tumeric Fried Rice</h3><span class="item-price">€10</span>
        <p class="item-desc">Long beans, cabbage, cucumber, tomatoes, cilantro</p></div>
      <div class="item"><h3 class="item-name">Crab Meat Fried Rice</h3><span class="item-price">€12</span>
        <p class="item-desc">Scallion, ginger, egg, crab meat, Thai seafood dipping soy sauce</p></div>
      <div class="item"><h3 class="item-name" style="width:250px">Mee Goreng/ Meggie Goreng</h3><span class="item-price">€10</span>
        <p class="item-desc">Tarang style stir fried egg noodle, fried tofu, potatoes, egg, beansprout, shredded lettuce, peanuts, fried shallots, fresh lime</p></div>
    </div>
  </section>

  <section class="section section--soups">
    <svg class="corner corner--top" viewBox="0 0 58 50"><polygon points="0,0 58,0 0,50" fill="var(--yellow)"/></svg>
    <svg class="corner corner--bottom" viewBox="0 0 58 50"><polygon points="58,0 58,50 0,50" fill="var(--yellow)"/></svg>
    <div class="section-heading"><h2>Soups &amp; Salads</h2></div>
    <div class="column column--left">
      <div class="item"><h3 class="item-name">Thai Tom Yum Soup</h3><span class="item-price">€6</span>
        <p class="item-desc">Shrimp, scallops, clams, fresh mushroom, cilantro, hand pounded Tom yum paste</p></div>
      <div class="item"><h3 class="item-name">Wonton Dumplings Soup</h3><span class="item-price">€5</span>
        <p class="item-desc">Baby bok choy, shiitake mushroom, wonton dumplings</p></div>
      <div class="item"><h3 class="item-name">Coconut Galangal Soup</h3><span class="item-price">€5</span>
        <p class="item-desc">Hand pounded Nam-prik chili oil, fresh mushrooms, chicken breast</p></div>
    </div>
    <div class="column column--right">
      <div class="item"><h3 class="item-name">Tarang Style Pasembur Salad</h3><span class="item-price">€8</span>
        <p class="item-desc">Warm salad, shredded jicama, cucumber, hard broiled egg, tofu, beansprout, crispy fritters, spicy sweet potato gravy</p></div>
      <div class="item"><h3 class="item-name">Vermicelli Beef Tossed Salad</h3><span class="item-price">€9</span>
        <p class="item-desc">Grilled steak, kale, lemongrass, carrot, tomatoes, palm sugar, cilantro, mint, fresh lime vinaigrette</p></div>
      <div class="item"><h3 class="item-name">Northen Thai Style Papaya Salad</h3><span class="item-price">€7</span>
        <p class="item-desc item-desc--wide">Fresh pounded papaya, carrot, roasted peanut, tomatoes, long beans, fresh lime dressing, Crab +2</p></div>
    </div>
  </section>
</div>
</body>
</html>
```